Email Banner (LumenBriefs)

We require an email banner for our email promotions sent to prospect clients. The banner needs to contain the wording LumenBriefs and use the same colour scheme as the logos attached.

This is for B2B professional's so needs to look like a place you would come to read technology articles.

```html
<!DOCTYPE html>
<html lang="en">
<head>
<meta charset="utf-8">
<title>LumenBriefs Email Banners</title>
<link rel="stylesheet" href="https://fonts.googleapis.com/css2?family=Montserrat:wght@700;800&family=Varela+Round&display=swap">
<style>
  :root {
    --navy: #0b1322;
    --white: #ffffff;
    --green: #6ef02a;
    --mint: #3fd4a6;
    --teal: #2fc2b8;
    --blue: #3aaef5;
    --deep-teal: #0f3a48;
  }
  * { margin: 0; padding: 0; box-sizing: border-box; }
  html, body { width: 1200px; height: 451px; overflow: hidden; background: var(--navy); }
  .canvas { position: relative; width: 1200px; height: 451px; background: var(--navy); font-family: "Montserrat", sans-serif; color: var(--white); }
  .banner { position: absolute; width: 542px; height: 166px; overflow: hidden; box-shadow: 0 4px 10px rgba(0,0,0,.35); }
  .banner--tech-talk { left: 40px; top: 40px; background: linear-gradient(20deg, var(--green) 0%, var(--mint) 55%, var(--teal) 100%); }
  .banner--breaking { left: 619px; top: 40px; background: linear-gradient(25deg, #4fd35a 0%, #2fb9a0 45%, #1f8f96 100%); }
  .banner--insights { left: 40px; top: 237px; background: linear-gradient(90deg, #0d2f3c 0%, #14485a 45%, #1d6f86 80%, #2a9fd6 100%); }
  .banner--power { left: 619px; top: 237px; background: linear-gradient(25deg, var(--green) 0%, var(--mint) 50%, var(--blue) 100%); }

  .photo { position: absolute; inset: 0; }
  .photo-curve { position: absolute; left: 0; top: 0; }

  .brand-tab { position: absolute; left: 0; top: 0; width: 197px; height: 52px; background: var(--white); border-bottom-right-radius: 24px; display: flex; align-items: center; padding-left: 20px; gap: 7px; z-index: 2; }
  .brand-dot { width: 8px; height: 8px; border-radius: 50%; background: var(--mint); }
  .brand-name { font-family: "Varela Round", sans-serif; font-size: 18px; color: var(--navy); letter-spacing: -.2px; }

  .headline { position: absolute; left: 16px; font-weight: 800; font-size: 36px; line-height: 31px; letter-spacing: .5px; text-transform: uppercase; z-index: 2; white-space: nowrap; }
  .headline--medium { font-size: 28px; line-height: 30px; }
  .tagline { position: absolute; left: 16px; font-family: "Varela Round", sans-serif; font-size: 16.5px; line-height: 20.5px; z-index: 2; white-space: nowrap; }

  .cta { position: absolute; background: var(--white); color: var(--navy); font-weight: 700; font-size: 11px; letter-spacing: .3px; border-radius: 10px; display: flex; align-items: center; justify-content: center; z-index: 2; }
  .cta--large { font-size: 13.5px; border-radius: 12px; }
</style>
</head>
<body>
<main class="canvas">

  <section class="banner banner--tech-talk">
    <svg class="photo-curve" width="542" height="166" viewBox="0 0 542 166" role="img" aria-label="Photo of a hand writing in a notebook beside a tablet">
      <defs>
        <linearGradient id="deskPhoto" x1="0" y1="0" x2="1" y2="1">
          <stop offset="0" stop-color="#b07a3a"/>
          <stop offset=".45" stop-color="#d9c7a8"/>
          <stop offset="1" stop-color="#4a5a78"/>
        </linearGradient>
      </defs>
      <path d="M252 0 H542 V166 H322 C275 152 252 122 252 78 Z" fill="url(#deskPhoto)"/>
    </svg>
    <div class="brand-tab"><span class="brand-dot"></span><span class="brand-name">LumenBriefs.io</span></div>
    <h2 class="headline" style="top:75px;">Tech Talk</h2>
    <p class="tagline" style="top:107px;">Insights and Analysis<br>from Our Tech Writers</p>
    <a class="cta" style="left:436px; top:131px; width:91px; height:24px;">CLICK HERE</a>
  </section>

  <section class="banner banner--breaking">
    <div class="photo" role="img" aria-label="Photo of a laptop keyboard, printed pages and reading glasses in teal tones"></div>
    <div class="brand-tab"><span class="brand-dot"></span><span class="brand-name">LumenBriefs.io</span></div>
    <h2 class="headline" style="top:71px;">Breaking<br>Tech News</h2>
    <p class="tagline" style="top:134px;">Stay Up-to-Date with Our Industry Experts</p>
    <a class="cta cta--large" style="left:402px; top:124px; width:112px; height:29px;">CLICK HERE</a>
  </section>

  <section class="banner banner--insights">
    <div class="photo" role="img" aria-label="Photo of a team gathered around a laptop in an office"></div>
    <div class="brand-tab"><span class="brand-dot"></span><span class="brand-name">LumenBriefs.io</span></div>
    <h2 class="headline" style="top:65px;">Innovative Insights</h2>
    <p class="tagline" style="top:96px;">Our Technology Articles Keep You Ahead of the Curve</p>
    <a class="cta" style="left:19px; top:131px; width:91px; height:24px;">CLICK HERE</a>
  </section>

  <section class="banner banner--power">
    <div class="brand-tab"><span class="brand-dot"></span><span class="brand-name">LumenBriefs.io</span></div>
    <h2 class="headline headline--medium" style="top:71px;">Unleash the Power<br>of Technology</h2>
    <p class="tagline" style="top:131px;">Our Articles Empower Your Business</p>
    <a class="cta" style="left:434px; top:131px; width:91px; height:24px;">CLICK HERE</a>
  </section>

</main>
</body>
</html>
```